Clean and modern business cards

Looking for an updated business card design for my dental office “corvanta dental” . Looking for a modern clean / sleek design . I’m thinking black background but open to seeing other options . One side needs to have an appointment card . Card needs to have logo, dentist name , phone, email , address . I’ve attached couple of cards I thought were cool as well as my logo
Target Market(s)
Dental patients
Industry/Entity Type
Dentistry
Contact Information for Business Card
Phone email address

```html
<!DOCTYPE html>
<html lang="en">
<head>
<meta charset="utf-8">
<title>Corvanta Dental – Business Card</title>
<link href="https://fonts.googleapis.com/css2?family=Aleo:wght@400;700&family=Raleway:wght@300;400&display=swap" rel="stylesheet">
<style>
  :root {
    --ink: #111111;
    --text-soft: #333333;
    --card-border: #d6d6d6;
    --pattern-light: #fcfcfc;
    --pattern-dark: #f3f3f3;
    --accent-red: #e0432b;
    --rule-red: #e05252;
    --rule-grey: #8a8a8a;
    --plus-grey: #bdbdbd;
    --band-purple: #6a2c8e;
    --band-teal: #1ba3c6;
    --band-yellow: #fecb0a;
    --band-red: #e0432b;
    --band-navy: #263f8f;
    --band-green: #9cc03f;
  }
  * { margin: 0; padding: 0; box-sizing: border-box; }
  html, body {
    width: 1200px; height: 1000px; overflow: hidden;
    background: #ffffff;
  }
  .canvas { position: relative; width: 1200px; height: 1000px; }

  .card {
    position: absolute; left: 241px; width: 718px; height: 416px;
    border: 1px solid var(--card-border); border-bottom: none;
    background: #ffffff; overflow: hidden;
  }
  .card--front { top: 53px; }
  .card--back { top: 531px; }

  .card__pattern {
    position: absolute; inset: 0;
    background: linear-gradient(135deg, var(--pattern-light), var(--pattern-dark));
  }

  .brand {
    position: absolute; left: 44px; top: 46px;
    display: flex; align-items: center; gap: 18px;
  }
  .brand__dot {
    width: 64px; height: 64px; border-radius: 50%;
    background: var(--band-teal);
  }
  .brand__name {
    font-family: "Aleo", Georgia, serif; font-weight: 700;
    font-size: 27px; letter-spacing: 1px; color: var(--ink);
    text-transform: uppercase; line-height: 1;
  }

  .dentist {
    position: absolute; left: 0; right: 0; top: 232px;
    text-align: center;
    font-family: "Aleo", Georgia, serif; font-weight: 700;
    font-size: 25px; letter-spacing: 1.2px; color: var(--ink); line-height: 32px;
  }
  .dentist__plus {
    color: var(--accent-red); font-size: 20px;
    position: relative; top: -12px; margin-right: 1px;
  }

  .contact {
    position: absolute; left: 0; right: 0; top: 332px;
    text-align: center;
    font-family: "Raleway", Arial, sans-serif; font-weight: 300;
    font-size: 16px; letter-spacing: 0.4px; color: var(--text-soft);
    line-height: 24px; text-transform: uppercase;
    padding-left: 8px;
  }

  .color-band {
    position: absolute; left: -1px; right: -1px; bottom: 0; height: 8px;
    display: flex;
  }
  .color-band span { flex: 1; }
  .color-band .purple { background: var(--band-purple); }
  .color-band .teal { background: var(--band-teal); }
  .color-band .yellow { background: var(--band-yellow); }
  .color-band .red { background: var(--band-red); }
  .color-band .navy { background: var(--band-navy); }
  .color-band .green { background: var(--band-green); }

  .appointment__title {
    position: absolute; left: 0; right: 0; top: 53px;
    text-align: center;
    font-family: "Aleo", Georgia, serif; font-weight: 700;
    font-size: 24px; color: var(--ink); line-height: 30px;
  }
  .appointment__grid { position: absolute; inset: 0; }
  .appointment__label {
    position: absolute; top: 112px; width: 200px; margin-left: -100px;
    text-align: center;
    font-family: "Raleway", Arial, sans-serif; font-weight: 400;
    font-size: 20px; color: var(--ink); line-height: 26px;
  }
  .appointment__label--date { left: 220px; }
  .appointment__label--time { left: 500px; }

  .appointment__note {
    position: absolute; left: 0; right: 0; top: 337px;
    text-align: center;
    font-family: "Aleo", Georgia, serif; font-weight: 700;
    font-size: 14px; color: var(--ink); line-height: 23px;
  }
  .appointment__note-plus { color: var(--plus-grey); margin-right: 2px; }
</style>
</head>
<body>
<main class="canvas">

  <section class="card card--front" aria-label="Business card front">
    <div class="card__pattern" role="img" aria-label="Faint repeating tooth outline pattern"></div>

    <div class="brand">
      <span class="brand__dot"></span>
      <span class="brand__name">Corvanta Dental</span>
    </div>

    <h1 class="dentist"><span class="dentist__plus">+</span>Dr. Elias Vernhoff</h1>

    <p class="contact">
      2210 Marlow Hwy , Brandon , MB | (204) 555-0182<br>
      corvantadental.ca | contact @corvantadental.ca
    </p>

    <div class="color-band">
      <span class="purple"></span><span class="teal"></span><span class="yellow"></span>
      <span class="red"></span><span class="navy"></span><span class="green"></span>
    </div>
  </section>

  <section class="card card--back" aria-label="Appointment card">
    <h2 class="appointment__title">Your Next Appointment is :</h2>

    <svg class="appointment__grid" width="718" height="416" viewBox="0 0 718 416" aria-hidden="true">
      <line x1="359" y1="101" x2="359" y2="317" stroke="var(--rule-red)" stroke-width="1.3"/>
      <line x1="81" y1="150" x2="637" y2="150" stroke="var(--rule-red)" stroke-width="1.3"/>
      <line x1="81" y1="207" x2="637" y2="207" stroke="var(--rule-red)" stroke-width="1" stroke-dasharray="3 2"/>
      <line x1="81" y1="264" x2="637" y2="264" stroke="var(--rule-grey)" stroke-width="1" stroke-dasharray="3 2"/>
    </svg>

    <span class="appointment__label appointment__label--date">Date</span>
    <span class="appointment__label appointment__label--time">Time</span>

    <p class="appointment__note">
      <span class="appointment__note-plus">+</span>To cancel or reschedule please notify us at<br>
      least 48 hours to your sheduled appointment
    </p>

    <div class="color-band">
      <span class="purple"></span><span class="teal"></span><span class="yellow"></span>
      <span class="red"></span><span class="navy"></span><span class="green"></span>
    </div>
  </section>

</main>
</body>
</html>
```